Attention grabbing 6x9 postcard

We are looking to have an attention grabbing post card that be sent out to homeowners from our roofing company Vell Roofing. the concept is that on the front it will say something like (STOP THE KNOCKING!
Tired of roofers knocking on your door? Contact us because we value your time as much as you value the roof over your head."
Vell Roofing
VellRoofing.example
555.672.VELL
info@vellroofing.example

Please feel free to come up with something very creative. Once we pick the final design we will provide the copy.

```html
<!DOCTYPE html>
<html lang="en">
<head>
<meta charset="utf-8">
<title>Vell Roofing Postcard</title>
<link rel="stylesheet" href="https://fonts.googleapis.com/css2?family=Oswald:wght@500;600;700&display=swap">
<style>
  :root {
    --canvas: #e9eaec;
    --honey: #e8b43a;
    --ink: #0d0d0d;
    --charcoal: #262626;
    --paper: #ffffff;
    --photo-dark: #3a3433;
    --photo-shirt: #8f97a8;
    --photo-sky: #aab3ba;
    --photo-roof: #4d5058;
  }
  * { margin: 0; padding: 0; box-sizing: border-box; }
  html, body { width: 1200px; height: 1200px; overflow: hidden; }
  body { background: var(--canvas); position: relative; font-family: "Oswald", sans-serif; }
  .postcard { position: absolute; display: block; background: var(--paper); }
  .postcard--front { left: 182px; top: 166px; width: 598px; height: 396px; }
  .postcard--back { left: 371px; top: 659px; width: 595px; height: 397px; }
  .postcard text { font-family: "Oswald", sans-serif; text-transform: uppercase; }
  .fill-honey { fill: var(--honey); }
  .fill-ink { fill: var(--ink); }
  .fill-charcoal { fill: var(--charcoal); }
  .fill-paper { fill: var(--paper); }
  .brand-name { font-weight: 600; letter-spacing: 1px; }
  .headline { font-weight: 600; }
  .body-copy { font-weight: 600; font-size: 12.6px; fill: var(--ink); }
  .contact { font-weight: 500; fill: var(--paper); }
  .address-line { stroke: var(--ink); stroke-width: 1.2; }
</style>
</head>
<body>

<svg class="postcard postcard--front" viewBox="0 0 478 317" aria-label="Postcard front">
  <rect class="fill-paper" width="478" height="317"/>
  <polygon points="228,0 478,0 478,213 359,213" fill="var(--photo-dark)" role="img" aria-label="Photo of a roofer in a striped shirt knocking on a dark front door, holding a clipboard"/>
  <polygon points="340,60 478,10 478,200 400,213" fill="var(--photo-shirt)" opacity="0.35"/>
  <polygon class="fill-honey" points="0,0 214,0 314,162 0,162"/>
  <polygon class="fill-ink" points="0,162 316,162 336,207 0,207"/>
  <polygon class="fill-honey" points="318,213 478,213 478,317 196,317 210,300 318,300"/>
  <rect class="fill-ink" x="0" y="305" width="192" height="12"/>

  <circle class="fill-paper" cx="40" cy="31" r="6"/>
  <text class="brand-name fill-paper" x="52" y="37" font-size="15">Vell Roofing</text>

  <text class="headline fill-paper" x="30" y="106" font-size="43">Vell</text>
  <text class="headline fill-paper" x="30" y="151" font-size="43">Roofing</text>
  <text class="headline fill-paper" x="30" y="196" font-size="27">Stop the Knocking!</text>

  <text class="body-copy" x="32" y="229">Tired of roofers knocking on your door?</text>
  <text class="body-copy" x="32" y="246">Contact us because we value your time</text>
  <text class="body-copy" x="32" y="263">as much as you value the roof over your</text>
  <text class="body-copy" x="32" y="280">head."</text>

  <polygon class="fill-ink" points="319,214 414,214 404,239 319,239"/>
  <text class="headline fill-paper" x="334" y="233" font-size="13">Call us :</text>
  <text class="headline fill-paper" x="344" y="263" font-size="16">555.672.VELL</text>

  <circle class="fill-ink" cx="329" cy="281" r="4.5"/>
  <rect class="fill-paper" x="326.5" y="279.2" width="5" height="3.6"/>
  <text class="contact" x="344" y="284" font-size="7.6" fill="var(--ink)" style="fill:var(--ink)">info@vellroofing.example</text>
  <circle class="fill-ink" cx="329" cy="297" r="4.5"/>
  <circle cx="329" cy="297" r="2.4" fill="none" stroke="var(--paper)" stroke-width="0.8"/>
  <text class="contact" x="344" y="300" font-size="7.6" style="fill:var(--ink)">VellRoofing.example</text>
</svg>

<svg class="postcard postcard--back" viewBox="0 0 476 318" aria-label="Postcard back">
  <rect class="fill-paper" width="476" height="318"/>
  <polygon class="fill-charcoal" points="0,0 293,0 248,113 0,113"/>
  <rect x="0" y="117" width="107" height="140" fill="var(--photo-dark)" role="img" aria-label="Photo of a hand knocking on a dark wooden door"/>
  <polygon points="112,117 244,117 209,257 112,257" fill="var(--photo-sky)" role="img" aria-label="Photo of a house dormer window and grey shingle roof"/>
  <polygon points="112,190 228,175 209,257 112,257" fill="var(--photo-roof)"/>
  <polygon class="fill-honey" points="293,0 304,0 198,266 0,266 0,257 187,257"/>

  <text class="headline fill-honey" x="30" y="50" font-size="32">Vell</text>
  <text class="headline fill-honey" x="30" y="86" font-size="32">Roofing</text>

  <circle class="fill-honey" cx="390" cy="40" r="9"/>
  <text class="brand-name fill-honey" x="390" y="79" font-size="9.5" text-anchor="middle">Vell Roofing</text>

  <line class="address-line" x1="270" y1="161" x2="431" y2="161"/>
  <line class="address-line" x1="256" y1="201" x2="431" y2="201"/>
  <line class="address-line" x1="243" y1="240" x2="431" y2="240"/>

  <rect class="fill-honey" x="0" y="281" width="476" height="37"/>
  <circle class="fill-paper" cx="26" cy="299" r="7"/>
  <path d="M23,295 l2,0 l1,2.5 l-1.2,1 a6,6 0 0 0 2.8,2.8 l1,-1.2 l2.5,1 l0,2 a1,1 0 0 1 -1,1 a9,9 0 0 1 -8,-8 a1,1 0 0 1 1,-1 z" class="fill-honey"/>
  <text class="contact" x="45" y="304" font-size="12.5">555.672.VELL</text>
  <circle class="fill-paper" cx="154" cy="299" r="7"/>
  <rect class="fill-honey" x="150" y="296.5" width="8" height="5.5"/>
  <text class="contact" x="168" y="304" font-size="11">info@vellroofing.example</text>
  <circle class="fill-paper" cx="334" cy="299" r="7"/>
  <circle cx="334" cy="299" r="4" fill="none" stroke="var(--honey)" stroke-width="1"/>
  <line x1="330" y1="299" x2="338" y2="299" stroke="var(--honey)" stroke-width="0.8"/>
  <text class="contact" x="348" y="304" font-size="11.5">VellRoofing.example</text>
</svg>

</body>
</html>
```